I have an animal hospital. I want a poster to hang in each exam room to show a picture of a normal sized heart and then an enlarged heart of a dog that was fed a grain-free diet. I want to warn people not to feed grain-free diets. Maybe at the top of the poster, "Do you feed grain-free?" and then the x-ray comparison, then the warnings of Canine Dilated Cardiomyopathy.

```html
<!DOCTYPE html>
<html lang="en">
<head>
<meta charset="utf-8">
<title>Do You Feed Grain-Free? Exam Room Poster</title>
<link href="https://fonts.googleapis.com/css2?family=Poppins:wght@500;600;700;800&display=swap" rel="stylesheet">
<style>
  :root {
    --navy: #2d4c8e;
    --navy-dark: #243f78;
    --cyan: #00e1fb;
    --cyan-band: #10dcf6;
    --red: #ec1c24;
    --white: #ffffff;
    --backdrop: #e4e4e6;
    --text-dark: #3a3a3a;
    --xray-black: #0b0b0b;
  }
  * { margin: 0; padding: 0; box-sizing: border-box; }
  html, body { width: 1200px; height: 3034px; overflow: hidden; }
  body { background: var(--backdrop); font-family: 'Poppins', sans-serif; position: relative; }

  .poster {
    position: absolute; left: 60px; top: 754px; width: 1080px; height: 1526px;
    background: var(--white); overflow: hidden;
    box-shadow: 0 10px 30px rgba(0,0,0,0.18);
  }
  .abs { position: absolute; }

  /* Header */
  .header { left: 0; top: 0; width: 1080px; height: 263px; background: var(--navy); }
  .header-wave { left: 0; top: 244px; width: 1080px; height: 22px; }
  .title { width: 100%; text-align: center; font-weight: 800; font-size: 112px; line-height: 1; letter-spacing: -2px; }
  .title-top { top: 34px; color: var(--white); }
  .title-bottom { top: 133px; color: var(--cyan); }

  /* Anatomy */
  .anatomy { border-radius: 40% 45% 48% 42%; }
  .anatomy-normal { left: 157px; top: 283px; width: 396px; height: 337px;
    background: radial-gradient(ellipse at 55% 55%, #a8313a 0%, #c85a60 45%, #e9a6a0 75%, #f6e4e2 100%); }
  .anatomy-dilated { left: 586px; top: 283px; width: 317px; height: 324px;
    background: radial-gradient(ellipse at 55% 60%, #9c2a33 0%, #c4525a 45%, #e6a29c 75%, #f6e4e2 100%); }
  .tag {
    background: var(--red); color: var(--white); font-weight: 700; font-size: 17px; line-height: 1.05;
    text-align: center; border-radius: 6px; display: flex; align-items: center; justify-content: center;
  }
  .tag-normal { left: 71px; top: 617px; width: 225px; height: 45px; }
  .tag-dilated { left: 786px; top: 617px; width: 223px; height: 45px; }

  /* X-ray band */
  .xray-band { left: 0; top: 696px; width: 1080px; height: 571px; background: var(--cyan-band); }
  .xray-card {
    background: var(--xray-black); border: 3px solid var(--navy); border-radius: 22px; overflow: hidden;
  }
  .xray-card-normal { left: 71px; top: 722px; width: 531px; height: 499px; }
  .xray-card-enlarged { left: 618px; top: 722px; width: 388px; height: 499px; }
  .xray-heading {
    position: absolute; left: 0; top: 0; width: 100%; height: 55px; background: var(--navy);
    color: var(--white); font-weight: 600; font-size: 16px; line-height: 1.15; text-align: center;
    display: flex; align-items: center; justify-content: center;
  }
  .xray-image { position: absolute; left: 0; top: 55px; width: 100%; bottom: 0; }
  .xray-image-normal { background: radial-gradient(ellipse at 50% 50%, #b9b9b9 0%, #6d6d6d 35%, #262626 65%, #0b0b0b 100%); }
  .xray-image-enlarged { background: radial-gradient(ellipse 38% 60% at 50% 45%, #c4c4c4 0%, #7a7a7a 45%, #1d1d1d 85%, #0b0b0b 100%); }
  .xray-marker { position: absolute; color: var(--white); font-weight: 500; }
  .marker-r { left: 46px; bottom: 24px; font-size: 26px; }
  .marker-l { right: 24px; bottom: 18px; font-size: 16px; }
  .focus-ring { left: 79px; top: 185px; width: 210px; height: 230px; border: 8px solid rgba(230,30,40,0.85); border-radius: 50%; box-shadow: 0 0 12px rgba(230,30,40,0.6); }
  .patient-name { top: 1230px; color: var(--navy); font-weight: 700; font-size: 22px; }
  .patient-bait { left: 135px; }
  .patient-shrimp { left: 838px; }

  /* Warnings */
  .warning-pill {
    left: 379px; top: 1269px; width: 313px; height: 47px; background: var(--red); border-radius: 24px;
    color: var(--white); font-weight: 800; font-size: 38px; line-height: 47px; padding-left: 62px; letter-spacing: -0.5px;
  }
  .warning-icon { left: 0; top: -4px; width: 60px; height: 52px; }
  .warning-frame { left: 65px; top: 1341px; width: 947px; height: 103px; }
  .warning-headline {
    left: 0; top: 1322px; width: 1080px; text-align: center; color: var(--navy);
    font-weight: 800; font-size: 38px; letter-spacing: -0.5px;
  }
  .symptoms { left: 88px; top: 1384px; width: 902px; display: flex; }
  .symptom {
    flex: 1 1 0; text-align: center; color: var(--text-dark); font-weight: 600; font-size: 20px; line-height: 1.15;
    border-right: 2px solid #d7d7d7; padding: 0 4px;
  }
  .symptom:last-child { border-right: none; }
  .symptom-icon {
    width: 40px; height: 36px; margin: 0 auto 8px; border-radius: 8px;
    background: linear-gradient(135deg, #dbe6f7, #9ec6ee);
  }
</style>
</head>
<body>
<main class="poster">
  <header class="abs header">
    <h1 class="abs title title-top">DO YOU FEED</h1>
    <h1 class="abs title title-bottom">GRAIN-FREE?</h1>
  </header>
  <svg class="abs header-wave" viewBox="0 0 1080 22" preserveAspectRatio="none" aria-hidden="true">
    <path fill="#ffffff" d="M0 22 V10 Q 11.25 0 22.5 10 T 45 10 T 67.5 10 T 90 10 T 112.5 10 T 135 10 T 157.5 10 T 180 10 T 202.5 10 T 225 10 T 247.5 10 T 270 10 T 292.5 10 T 315 10 T 337.5 10 T 360 10 T 382.5 10 T 405 10 T 427.5 10 T 450 10 T 472.5 10 T 495 10 T 517.5 10 T 540 10 T 562.5 10 T 585 10 T 607.5 10 T 630 10 T 652.5 10 T 675 10 T 697.5 10 T 720 10 T 742.5 10 T 765 10 T 787.5 10 T 810 10 T 832.5 10 T 855 10 T 877.5 10 T 900 10 T 922.5 10 T 945 10 T 967.5 10 T 990 10 T 1012.5 10 T 1035 10 T 1057.5 10 T 1080 10 V22 Z"/>
  </svg>

  <section class="anatomy-section">
    <div class="abs anatomy anatomy-normal" role="img" aria-label="Labelled cross-section illustration of a normal canine heart"></div>
    <div class="abs anatomy anatomy-dilated" role="img" aria-label="Cross-section illustration of a heart with dilated cardiomyopathy and enlarged ventricles"></div>
    <div class="abs tag tag-normal">NORMAL HEART</div>
    <div class="abs tag tag-dilated">DILATE<br>CARDIOMYOPATHY</div>
  </section>

  <section class="abs xray-band"></section>
  <figure class="abs xray-card xray-card-normal">
    <figcaption class="xray-heading">NORMAL SIZED HEART</figcaption>
    <div class="xray-image xray-image-normal" role="img" aria-label="Chest x-ray of a dog with a normal sized heart">
      <span class="xray-marker marker-r">R</span>
    </div>
  </figure>
  <figure class="abs xray-card xray-card-enlarged">
    <figcaption class="xray-heading">ENLARGED HEART OF A DOG THAT<br>WAS FED A GRAIN-FREE DIET</figcaption>
    <div class="xray-image xray-image-enlarged" role="img" aria-label="Chest x-ray of a dog with an enlarged heart after a grain-free diet">
      <div class="abs focus-ring"></div>
      <span class="xray-marker marker-l">L</span>
    </div>
  </figure>
  <span class="abs patient-name patient-bait">BAIT</span>
  <span class="abs patient-name patient-shrimp">SHRIMP</span>

  <section class="warnings">
    <svg class="abs warning-frame" viewBox="0 0 947 103" aria-hidden="true">
      <path d="M50 2 H2 V101 H20" fill="none" stroke="#2d4c8e" stroke-width="3"/>
      <path d="M897 2 H945 V101 H925" fill="none" stroke="#2d4c8e" stroke-width="3"/>
    </svg>
    <div class="abs warning-pill">
      <svg class="abs warning-icon" viewBox="0 0 60 52" aria-hidden="true">
        <path d="M30 3 L57 49 H3 Z" fill="#ec1c24" stroke="#ffffff" stroke-width="3" stroke-linejoin="round"/>
        <rect x="27" y="17" width="6" height="19" rx="2" fill="#ffffff"/>
        <circle cx="30" cy="42" r="3.5" fill="#ffffff"/>
      </svg>
      WARNINGS
    </div>
    <h2 class="abs warning-headline">OF CANINE DILATED CARDIOMYOPATHY.</h2>
    <ul class="abs symptoms">
      <li class="symptom" style="list-style:none"><div class="symptom-icon" role="img" aria-label="Tired dog icon"></div>Lethargy</li>
      <li class="symptom" style="list-style:none"><div class="symptom-icon" role="img" aria-label="Dog refusing food icon"></div>Anorexia</li>
      <li class="symptom" style="list-style:none"><div class="symptom-icon" role="img" aria-label="Dog breathing hard icon"></div>Labored<br>breathing</li>
      <li class="symptom" style="list-style:none"><div class="symptom-icon" role="img" aria-label="Panting dog icon"></div>Panting</li>
      <li class="symptom" style="list-style:none"><div class="symptom-icon" role="img" aria-label="Coughing dog icon"></div>Coughing</li>
      <li class="symptom" style="list-style:none"><div class="symptom-icon" role="img" aria-label="Dog with swollen belly icon"></div>Abdominal<br>distension</li>
      <li class="symptom" style="list-style:none"><div class="symptom-icon" role="img" aria-label="Collapsed dog icon"></div>Sudden<br>collapse</li>
    </ul>
  </section>
</main>
</body>
</html>
```